What happens?

Develop a graphic to be used on a church web page based on the following:

"What happens at the intersection of spirituality, sexuality and social justice?"
A second graphic will use the first concept and add an answer to it. "healing, creativity, acceptance, forgiveness, wholeness, service, freedom."

The graphic should be shades of gray, possibly with touches of color (yellow and blue).
This design needs to convey the idea of intersection not just be text.

Attached is a very rough graphic concept to use as a starting point.

Target Market(s)

young adults interested in progressive spirituality rather than dogmatic religion

Industry/Entity Type

Church

Font styles to use
Sans Serif

Requirements
Must have
• visual concept of intersection, visually tying of the answers to the question
Should not have
• just text

```html
<!DOCTYPE html>
<html lang="en">
<head>
<meta charset="utf-8">
<title>What happens at the intersection?</title>
<link rel="stylesheet" href="https://fonts.googleapis.com/css2?family=Zilla+Slab:wght@400&family=Fira+Sans:wght@700&family=Fira+Sans+Condensed:wght@400&family=Oswald:wght@500&display=swap">
<style>
  :root {
    --paper: #ffffff;
    --ink: #111111;
    --cross: #bba49a;
    --yellow: #f8ea6c;
    --yellow-dash: #f3e266;
    --sky: #ccdcec;
    --sky-dash: #b9e0f2;
    --blue-dash: #72bfe0;
    --blue-dash-deep: #6cb7dc;
    --slate: #c5d3d9;
    --stone: #d3d3d3;
    --venn-spirit: #9aa3b4;
    --venn-justice: #8fa08a;
    --venn-body: #4f6f93;
    --venn-sex: #a9a9a9;
    --venn-core: #c2b68e;
  }
  html, body {
    margin: 0;
    padding: 0;
    width: 1200px;
    height: 900px;
    overflow: hidden;
    background: var(--paper);
  }
  .artboard { display: block; width: 1200px; height: 900px; }
  .headline-what { font-family: "Zilla Slab", Georgia, serif; font-size: 86px; fill: var(--ink); }
  .headline-happens { font-family: "Fira Sans Condensed", Arial, sans-serif; font-size: 34px; letter-spacing: 1px; fill: var(--ink); }
  .headline-question { font-family: "Fira Sans", Arial, sans-serif; font-weight: 700; font-size: 37px; fill: var(--ink); }
  .label { font-family: "Oswald", "Arial Narrow", sans-serif; font-weight: 500; fill: var(--ink); }
  .label-venn { font-size: 40px; }
  .label-answer { font-size: 47px; text-anchor: middle; }
  .link { fill: none; }
</style>
</head>
<body>
<svg class="artboard" viewBox="0 0 1200 900" xmlns="http://www.w3.org/2000/svg">

  <!-- Heading -->
  <g class="heading">
    <text class="headline-what" x="64" y="273">What</text>
    <text class="headline-happens" x="296" y="273">HAPPENS...</text>
    <text class="headline-question" x="70" y="360">at the intersection?</text>
  </g>

  <!-- Answer cross -->
  <g class="answer-cross">
    <rect x="862" y="300" width="50" height="350" fill="var(--cross)"/>
    <rect x="790" y="413" width="200" height="50" fill="var(--cross)"/>
    <ellipse cx="890" cy="270" rx="95" ry="77" fill="var(--yellow)"/>
    <ellipse cx="710" cy="437" rx="95" ry="77" fill="var(--sky)"/>
    <ellipse cx="1070" cy="437" rx="95" ry="77" fill="var(--slate)"/>
    <ellipse cx="890" cy="692" rx="95" ry="77" fill="var(--stone)"/>
  </g>

  <!-- Connecting threads -->
  <g class="links">
    <path class="link" d="M210 437 C 330 425, 380 470, 480 475 S 600 482, 625 480" stroke="var(--sky-dash)" stroke-width="4" stroke-dasharray="3 3"/>
    <path class="link" d="M210 437 C 160 438, 150 445, 140 448" stroke="var(--sky-dash)" stroke-width="4" stroke-dasharray="3 3"/>
    <path class="link" d="M325 548 C 420 440, 520 340, 790 315" stroke="var(--yellow-dash)" stroke-width="7" stroke-dasharray="10 6"/>
    <path class="link" d="M440 578 C 560 620, 700 640, 860 636 C 960 630, 1035 580, 1032 510" stroke="var(--blue-dash)" stroke-width="6" stroke-dasharray="10 5"/>
    <path class="link" d="M140 548 C 105 545, 110 570, 140 565 C 260 560, 360 620, 460 680 C 580 760, 720 810, 860 805 C 960 800, 985 760, 985 715" stroke="var(--blue-dash-deep)" stroke-width="6" stroke-dasharray="10 5"/>
  </g>

  <!-- Intersection -->
  <g class="venn">
    <ellipse cx="225" cy="520" rx="102" ry="78" fill="var(--venn-spirit)" opacity="0.45"/>
    <ellipse cx="312" cy="548" rx="98" ry="82" fill="var(--venn-justice)" opacity="0.5"/>
    <ellipse cx="228" cy="602" rx="102" ry="78" fill="var(--venn-sex)" opacity="0.5"/>
    <ellipse cx="225" cy="560" rx="100" ry="75" fill="var(--venn-body)" opacity="0.45"/>
    <path d="M215 530 C 230 490, 290 480, 322 510 C 332 545, 318 580, 300 590 C 260 600, 215 585, 207 555 Z" fill="var(--venn-core)" opacity="0.85"/>
  </g>

  <!-- Labels -->
  <g class="labels">
    <text class="label label-venn" x="62" y="481">Spirituality</text>
    <text class="label label-venn" x="342" y="595">Social Justice</text>
    <text class="label label-venn" x="75" y="664">Sexuality</text>
    <text class="label label-answer" x="886" y="297">creativity</text>
    <text class="label label-answer" x="698" y="450">healing</text>
    <text class="label label-answer" x="1064" y="455">growth</text>
    <text class="label label-answer" x="884" y="717">innovation</text>
  </g>
</svg>
</body>
</html>
```